Financial Services Sales Sheet

We need this sheet redesigned. Needs to feel very corporate/financial. open to imagery/icons/colors/etc. Copy is in the docx file to expedite work. PDF is what client has done inh-house and feels dated.

```html
<!DOCTYPE html>
<html lang="en">
<head>
<meta charset="utf-8">
<title>Meridian Ledger Partners – Master Servicing &amp; Portfolio Optimization</title>
<link href="https://fonts.googleapis.com/css2?family=Libre+Baskerville&family=Source+Sans+3:ital,wght@0,400;0,600;0,700;1,400&display=swap" rel="stylesheet">
<style>
:root{
  --navy:#0f2550;
  --navy-deep:#0a1a3a;
  --blue:#2f74c8;
  --blue-light:#4b9be6;
  --ink:#1f2a3d;
  --muted:#4a5568;
  --page:#f6f8fc;
  --card:#f1f5fb;
  --line:#c9d6e8;
  --white:#ffffff;
}
*{box-sizing:border-box;margin:0;padding:0}
html,body{width:800px;height:1200px;overflow:hidden}
body{font-family:"Source Sans 3",Arial,sans-serif;color:var(--ink);background:var(--page);position:relative}
.sheet{position:absolute;inset:0;background:var(--page)}

/* header */
.hero{position:absolute;left:0;top:0;width:800px;height:370px;background:linear-gradient(100deg,var(--navy-deep) 0%,var(--navy) 60%,#163570 100%);overflow:hidden}
.hero-photo{position:absolute;right:0;top:0;width:320px;height:370px;
  clip-path:polygon(42% 0,100% 0,100% 100%,0 100%,0 100%,0 70%);
  background:linear-gradient(180deg,#0f2a5c 0%,#27508f 45%,#15346b 70%,#0b1f45 100%)}
.hero-accent{position:absolute;right:0;top:0;width:340px;height:370px;
  clip-path:polygon(52% 0,60% 0,8% 62%,30% 100%,24% 100%,0 62%);background:var(--blue);opacity:.55}
.brand{position:absolute;left:48px;top:52px;display:flex;align-items:center;gap:10px;color:var(--white)}
.brand-dot{width:34px;height:34px;border-radius:50%;background:var(--white)}
.brand-name{font-weight:700;font-size:14px;line-height:15px;letter-spacing:.3px}
.brand-tag{font-size:8px;letter-spacing:.4px;margin-top:3px}
.hero-title{position:absolute;left:47px;top:116px;font-family:"Libre Baskerville",Georgia,serif;font-size:36px;line-height:49px;color:var(--white);font-weight:400;white-space:nowrap}
.hero-kicker{position:absolute;left:48px;top:219px;font-size:13.5px;letter-spacing:1.2px;line-height:19px}
.hero-kicker .k1{color:var(--blue-light);display:block}
.hero-kicker .k2{color:#cfd8e6;display:block}
.hero-copy{position:absolute;left:48px;top:272px;width:430px;font-size:12.5px;line-height:20px;color:#e3e9f3}

/* services */
.services{position:absolute;left:0;top:370px;width:800px;height:330px}
.col{position:absolute;top:0;width:220px}
.col-1{left:50px}.col-2{left:290px}.col-3{left:530px}
.divider{position:absolute;top:40px;width:1px;height:280px;background:var(--line)}
.icon-badge{width:58px;height:58px;border-radius:50%;background:var(--navy);margin:21px auto 0;display:flex;align-items:center;justify-content:center}
.col h2{text-align:center;font-size:13.5px;font-weight:700;color:var(--navy);line-height:18px;margin-top:12px;letter-spacing:.2px;white-space:nowrap}
.col .rule{width:186px;height:1.5px;background:var(--blue-light);margin:8px auto 0}
.col ul{list-style:none;margin:13px 0 0 8px}
.col li{position:relative;padding-left:16px;font-size:11.5px;line-height:15px;color:var(--ink);margin-bottom:14px;white-space:nowrap}
.col li::before{content:"";position:absolute;left:0;top:5px;width:4px;height:4px;background:var(--blue)}
.col-2 li,.col-3 li{margin-bottom:10px}

/* snapshot */
.snapshot-head{position:absolute;left:52px;top:700px;display:flex;align-items:center;width:748px}
.snapshot-head span{width:4px;height:4px;background:var(--blue);margin-right:12px}
.snapshot-head h3{font-size:13px;font-weight:700;color:var(--navy);letter-spacing:.3px;white-space:nowrap}
.snapshot-head i{flex:1;height:1px;background:var(--line);margin-left:12px}
.stats{position:absolute;left:51px;top:732px;display:flex;gap:10px}
.stat{width:130px;height:133px;background:var(--card);border:1px solid #dde5f0;text-align:center;padding-top:14px}
.stat svg{display:block;margin:0 auto}
.stat b{display:block;font-size:16px;color:var(--navy);margin-top:12px;font-weight:700}
.stat small{display:block;font-size:11px;line-height:15px;color:var(--muted);margin-top:2px;white-space:nowrap}

/* pillars */
.pillars{position:absolute;left:70px;top:888px;width:660px;height:64px;display:flex}
.pillar{flex:1;display:flex;align-items:center;gap:14px;padding-left:8px;border-right:1px solid var(--line)}
.pillar:last-child{border-right:0}
.pillar p{font-size:11.5px;font-weight:600;color:var(--navy);line-height:15px;letter-spacing:.5px}

/* platform */
.platform{position:absolute;left:77px;top:971px;width:645px;height:107px;background:var(--navy);border-radius:3px;color:var(--white)}
.platform h4{position:absolute;top:12px;left:0;width:100%;text-align:center;font-size:13px;font-weight:600;letter-spacing:1.3px}
.platform .bar{position:absolute;top:21px;height:1px;width:135px;background:#5f7aa6}
.platform .bar.l{left:32px}.platform .bar.r{right:26px}
.platform-items{position:absolute;top:45px;left:30px;right:16px;display:flex}
.pf{display:flex;align-items:center;gap:16px;border-right:1px solid #3b5684;padding-left:4px}
.pf-1{width:190px}.pf-2{width:210px;padding-left:28px}.pf-3{flex:1;padding-left:36px;border-right:0}
.pf p{font-size:11px;line-height:15px;letter-spacing:.5px;white-space:nowrap}

/* footer */
.footer{position:absolute;left:0;top:1098px;width:800px;height:102px;background:var(--navy-deep)}
.footer .motto{position:absolute;left:52px;top:26px;font-style:italic;font-size:13px;color:var(--white);padding-bottom:6px;border-bottom:1px solid var(--blue);width:222px}
.footer .url{position:absolute;right:50px;top:29px;font-size:13px;color:var(--blue-light)}
</style>
</head>
<body>
<div class="sheet">

  <header class="hero">
    <div class="hero-photo" role="img" aria-label="Evening city skyline along the waterfront in blue tones"></div>
    <div class="hero-accent"></div>
    <div class="brand">
      <div class="brand-dot"></div>
      <div>
        <div class="brand-name">MERIDIAN LEDGER<br>PARTNERS</div>
        <div class="brand-tag">CLARITY IN EVERY PORTFOLIO</div>
      </div>
    </div>
    <h1 class="hero-title">Master Servicing &amp;<br>Portfolio Optimization</h1>
    <div class="hero-kicker"><span class="k1">END-TO-END POST DEFAULT MANAGEMENT</span><span class="k2">STRATEGY, RECOVERY &amp; COMPLIANCE</span></div>
    <p class="hero-copy">Meridian delivers master servicing solutions powered by proprietary technology and automation. We centralize back-office operations, optimize recovery performance, and embed compliance controls across the full post-default lifecycle—reducing client overhead while increasing transparency and results.</p>
  </header>

  <section class="services">
    <div class="divider" style="left:276px"></div>
    <div class="divider" style="left:516px"></div>

    <div class="col col-1">
      <div class="icon-badge"><svg width="30" height="28" viewBox="0 0 30 28" fill="#fff"><path d="M15 1 29 8H1z"/><rect x="2" y="9" width="26" height="2"/><rect x="5" y="12" width="3" height="10"/><rect x="10" y="12" width="3" height="10"/><rect x="17" y="12" width="3" height="10"/><rect x="22" y="12" width="3" height="10"/><rect x="1" y="23" width="28" height="3"/></svg></div>
      <h2>STRATEGY &amp; RECOVERY<br>OPTIMIZATION</h2>
      <div class="rule"></div>
      <ul>
        <li>Recovery &amp; Liquidation Optimization</li>
        <li>Settlement Campaigns</li>
        <li>Payer Base Development &amp; Retention</li>
        <li>Penetration &amp; Conversion Tracking</li>
        <li>Omni-Channel &amp; Champion<br>Challenger Collection Strategy</li>
      </ul>
    </div>

    <div class="col col-2">
      <div class="icon-badge"><svg width="28" height="32" viewBox="0 0 28 32" fill="none" stroke="#fff" stroke-width="2.2"><path d="M14 2 26 6v10c0 7-5 12-12 14C7 28 2 23 2 16V6z"/><path d="M8.5 16l4 4 7-8"/></svg></div>
      <h2>COMPLIANCE &amp; RISK<br>OVERSIGHT</h2>
      <div class="rule"></div>
      <ul>
        <li>Collection Agency Oversight</li>
        <li>Regulatory Compliance Audits<br>(FDCPA, FCRA, UDAAP)</li>
        <li>SOL Calculation &amp; Tracking</li>
        <li>Reg F Balance Reconciliations</li>
        <li>Bankruptcy, Military &amp; Deceased Checks</li>
        <li>Complaint Management &amp; Monitoring</li>
      </ul>
    </div>

    <div class="col col-3">
      <div class="icon-badge"><svg width="30" height="28" viewBox="0 0 30 28" fill="#fff"><rect x="3" y="18" width="5" height="8"/><rect x="11" y="13" width="5" height="13"/><rect x="19" y="8" width="5" height="18"/><path d="M3 14 12 7l4 3 9-7" fill="none" stroke="#fff" stroke-width="2"/><path d="M21 2h6v6z"/></svg></div>
      <h2>OPERATIONS &amp; PORTFOLIO<br>MANAGEMENT</h2>
      <div class="rule"></div>
      <ul>
        <li>Rigorous Placement &amp; Recall Processing</li>
        <li>Daily Balance Calculations &amp;<br>Data Management</li>
        <li>Bank &amp; Inventory Reconciliation</li>
        <li>Portfolio Database Access</li>
        <li>Executive Reporting</li>
        <li>Bankruptcy Monitoring &amp; Support</li>
      </ul>
    </div>
  </section>

  <div class="snapshot-head"><span></span><h3>PERFORMANCE SNAPSHOT</h3><i></i></div>
  <div class="stats">
    <div class="stat">
      <svg width="40" height="40" viewBox="0 0 40 40"><circle cx="20" cy="20" r="17" fill="none" stroke="#1d3f7e" stroke-width="2.5"/><path d="M20 20V3a17 17 0 0 1 17 17z" fill="#1d3f7e"/><path d="M20 20 34 30A17 17 0 0 1 6 28z" fill="#1d3f7e"/></svg>
      <b>$155+ MILLION</b><small>Portfolio Collections<br>Administered</small>
    </div>
    <div class="stat">
      <svg width="40" height="40" viewBox="0 0 40 40" fill="none" stroke="#2f5fa8" stroke-width="2"><circle cx="20" cy="13" r="8"/><path d="M5 38v-4c0-7 6-11 15-11s15 4 15 11v4z"/></svg>
      <b>573,000+</b><small>Defaulted Accounts<br>Managed</small>
    </div>
    <div class="stat">
      <svg width="40" height="40" viewBox="0 0 40 40" fill="none" stroke="#1d3f7e" stroke-width="2.2"><path d="M20 2 36 8v12c0 9-7 15-16 18C11 35 4 29 4 20V8z"/><path d="M13 20l5 5 9-10"/></svg>
      <b>3,700+</b><small>Compliance Audits<br>Conducted</small>
    </div>
    <div class="stat">
      <svg width="40" height="40" viewBox="0 0 40 40" fill="none" stroke="#2f5fa8" stroke-width="2"><rect x="4" y="28" width="7" height="10"/><rect x="16" y="22" width="7" height="16"/><rect x="28" y="14" width="7" height="24"/><path d="M4 20 30 4M24 4h6v6"/></svg>
      <b>21%</b><small>3-Year Gross Collection<br>Curve</small>
    </div>
    <div class="stat">
      <svg width="40" height="40" viewBox="0 0 40 40" fill="none" stroke="#2f5fa8" stroke-width="2"><rect x="3" y="6" width="34" height="31" rx="2"/><path d="M3 14h34M11 2v8M29 2v8"/><path d="M10 20h5M18 20h5M26 20h5M10 26h5M18 26h5M26 26h5M10 31h5M18 31h5" stroke-width="2.5"/></svg>
      <b>20+ YEARS</b><small>of Post-Default<br>Expertise</small>
    </div>
  </div>

  <div class="pillars">
    <div class="pillar">
      <svg width="46" height="46" viewBox="0 0 46 46" fill="none" stroke="#1d3f7e" stroke-width="2"><circle cx="22" cy="24" r="19"/><circle cx="22" cy="24" r="12"/><circle cx="22" cy="24" r="5"/><path d="M22 24 38 8M34 6v6h6"/></svg>
      <p>OPTIMIZED<br>RECOVERIES</p>
    </div>
    <div class="pillar">
      <svg width="42" height="42" viewBox="0 0 42 42" fill="none" stroke="#1d3f7e" stroke-width="2"><rect x="3" y="28" width="7" height="12"/><rect x="15" y="22" width="7" height="18"/><rect x="27" y="14" width="7" height="26"/><path d="M3 22 32 4M26 3h7v7"/></svg>
      <p>PROVEN<br>SCALE</p>
    </div>
    <div class="pillar">
      <svg width="40" height="46" viewBox="0 0 40 46"><path d="M20 2 37 8v14c0 11-8 18-17 22C11 40 3 33 3 22V8z" fill="none" stroke="#1d3f7e" stroke-width="2"/><path d="M20 7 32 11v11c0 8-6 13-12 16-6-3-12-8-12-16V11z" fill="#1d3f7e"/><path d="M14 23l4 4 8-8" fill="none" stroke="#4b9be6" stroke-width="2"/></svg>
      <p>EMBEDDED<br>COMPLIANCE</p>
    </div>
    <div class="pillar">
      <svg width="46" height="46" viewBox="0 0 46 46" fill="none" stroke="#1d3f7e" stroke-width="2.2"><circle cx="19" cy="19" r="15"/><path d="M30 30 42 42" stroke-width="4"/></svg>
      <p>MEASURABLE<br>OUTCOMES</p>
    </div>
  </div>

  <section class="platform">
    <span class="bar l"></span><span class="bar r"></span>
    <h4>PROPRIETARY TECHNOLOGY PLATFORM</h4>
    <div class="platform-items">
      <div class="pf pf-1">
        <svg width="54" height="46" viewBox="0 0 54 46" fill="none" stroke="#fff" stroke-width="2"><rect x="2" y="2" width="50" height="32" rx="2"/><path d="M20 44h14M27 34v10"/><path d="M27 8l8 3v6c0 5-4 8-8 10-4-2-8-5-8-10v-6z"/><path d="M23 17l3 3 5-5"/></svg>
        <p>BUILT-IN<br>COMPLIANCE<br>CONTROLS</p>
      </div>
      <div class="pf pf-2">
        <svg width="50" height="46" viewBox="0 0 50 46" fill="none" stroke="#fff" stroke-width="2"><circle cx="18" cy="18" r="9"/><circle cx="18" cy="18" r="3.5"/><path d="M18 3v5M18 28v5M3 18h5M28 18h5M7 7l4 4M25 25l4 4M29 7l-4 4M11 25l-4 4"/><circle cx="37" cy="33" r="6"/><circle cx="37" cy="33" r="2"/><path d="M37 24v3M37 39v3M28 33h3M43 33h3"/></svg>
        <p>CENTRALIZED<br>ASSET<br>VISIBILITY</p>
      </div>
      <div class="pf pf-3">
        <svg width="46" height="46" viewBox="0 0 46 46" fill="none" stroke="#fff" stroke-width="2"><path d="M8 16A17 17 0 0 1 38 12M38 30A17 17 0 0 1 8 34"/><path d="M32 6l6 6-8 2M14 40l-6-6 8-2"/><circle cx="23" cy="23" r="7"/><circle cx="23" cy="23" r="2.5"/></svg>
        <p>AUTOMATED<br>WORKFLOW &amp;<br>RECOVERY EXECUTION</p>
      </div>
    </div>
  </section>

  <footer class="footer">
    <div class="motto">Your Trusted Advisor.</div>
    <div class="url">www.meridianledger.com</div>
  </footer>

</div>
</body>
</html>
```